Business Card for IT company

I need a high tech looking business card using our logo. I prefer something clean and modern.

Target Market(s)

Buyers of IT hardware and software, IT Techies who are key influencers

Industry/Entity Type

Business

```html
<!DOCTYPE html>
<html lang="en">
<head>
<meta charset="utf-8">
<title>Norvale Consulting – Business Card</title>
<link rel="stylesheet" href="https://fonts.googleapis.com/css2?family=Asap+Condensed:wght@400;500;600&display=swap">
<style>
  :root {
    --page-bg: #e6e6e6;
    --card-white: #ffffff;
    --ink-dark: #2c2c2c;
    --brand-green: #3b9f35;
    --back-top: #646464;
    --back-bottom: #3f3f3f;
    --back-ghost: #4b4b4b;
    --back-text: #f4f4f4;
  }
  html, body {
    margin: 0;
    padding: 0;
    width: 1200px;
    height: 960px;
    overflow: hidden;
    background: var(--page-bg);
    font-family: "Asap Condensed", "Arial Narrow", sans-serif;
  }
  .sheet {
    position: relative;
    width: 1200px;
    height: 960px;
  }
  .card {
    position: absolute;
    left: 250px;
    width: 700px;
    height: 400px;
    border-radius: 28px;
    box-shadow: 0 10px 28px rgba(0,0,0,0.18);
    overflow: hidden;
  }
  /* Front */
  .card-front {
    top: 60px;
    background: var(--card-white);
  }
  .front-wordmark {
    position: absolute;
    left: 48px;
    top: 186px;
    display: flex;
    align-items: center;
    gap: 12px;
    white-space: nowrap;
  }
  .wordmark-square {
    width: 22px;
    height: 22px;
    background: var(--brand-green);
    flex: none;
  }
  .wordmark-name {
    font-size: 28px;
    font-weight: 600;
    letter-spacing: 2px;
    color: var(--ink-dark);
  }
  .front-details {
    position: absolute;
    left: 450px;
    top: 40px;
    color: var(--ink-dark);
  }
  .person-name {
    font-size: 38px;
    font-weight: 600;
    margin: 0;
    line-height: 1;
  }
  .person-role {
    font-size: 22px;
    color: var(--brand-green);
    margin: 4px 0 0;
  }
  .company-block {
    margin-top: 30px;
    font-size: 19px;
    line-height: 1.2;
  }
  .company-block p { margin: 0; }
  .company-name, .contact-label { color: var(--brand-green); }
  .company-block .address { margin-top: 4px; }
  .company-block .contact-label { margin-top: 8px; }
  .company-block .contact-number { margin-top: 2px; }
  /* Back */
  .card-back {
    top: 500px;
    background: linear-gradient(135deg, var(--back-top), var(--back-bottom));
  }
  .back-ghost {
    position: absolute;
    left: -20px;
    top: 30px;
    font-size: 230px;
    font-weight: 600;
    letter-spacing: 6px;
    color: var(--back-ghost);
    line-height: 1;
    white-space: nowrap;
  }
  .back-wordmark {
    position: absolute;
    left: 0;
    right: 0;
    top: 150px;
    display: flex;
    justify-content: center;
    align-items: center;
    gap: 12px;
  }
  .back-wordmark .wordmark-name { color: var(--back-text); font-size: 34px; }
  .back-wordmark .wordmark-square { width: 22px; height: 22px; }
  .website {
    position: absolute;
    left: 0;
    right: 0;
    bottom: 44px;
    margin: 0;
    text-align: center;
    color: var(--back-text);
    font-size: 22px;
    font-weight: 500;
    letter-spacing: 2px;
  }
</style>
</head>
<body>
<main class="sheet">
  <section class="card card-front">
    <div class="front-wordmark">
      <span class="wordmark-square"></span>
      <span class="wordmark-name">NORVALE CONSULTING</span>
    </div>
    <div class="front-details">
      <h1 class="person-name">Your Name</h1>
      <p class="person-role">Your Designation</p>
      <div class="company-block">
        <p class="company-name">Norvale Consulting, LLC.</p>
        <p class="address">420 Harbor Point Drive<br>Suite 900<br>Fairbrook, VA 22190</p>
        <p class="contact-label">Main Reception:</p>
        <p class="contact-number">555.218.4470</p>
        <p class="contact-label">Office Manager:</p>
        <p class="contact-number">555.218.4412/4413</p>
      </div>
    </div>
  </section>

  <section class="card card-back">
    <div class="back-ghost" aria-hidden="true">NORVALE</div>
    <div class="back-wordmark">
      <span class="wordmark-square"></span>
      <span class="wordmark-name">NORVALE CONSULTING</span>
    </div>
    <p class="website">www.norvalegroup.net</p>
  </section>
</main>
</body>
</html>
```